Shareworthy Infographic For Solopreneurs / Business Owners

I would like you to create an infographic for my "10 Steps to Building an Online Business You Can Be Proud Of" content.

STYLE REFERENCE:
Here are my 3 favorite infographics which I would like you to model....

My favorite: http://maribelglowguide.example/12-amazing-beauty-benefits-of-honey-infographic/

My 2nd favorite: http://www.quillnotary.example/grammar-goofs/

My 3rd favorite: http://verdalume.example/infographic-8-unusual-ways-to-show-off-your-indoor-plants/

BRANDING COLORS TO USE:
Here are my branding colors (hex codes):
I. Primary
-blue
-#002b5c
II. Secondary
-gray
-#afb7bc
III. Tertiary
-green
-#7bc142
I like to use green to emphasize points and "pop out".

CONTENTS OF THE INFOGRAPHIC

10 Steps to Building an Online Business You Can Be Proud Of

1. Pray
Ask God to guide you and let Him know that you are ready, willing, and able to change paths, if He makes it clear to you. Proverbs 16:9 says, we can make our plans, but the LORD determines our steps.

2. Why
Ask yourself "why" you are doing this. Leverage your goals and dreams to pull you towards success. Place pictures on your desktop or other places you will see them regularly.

3. Avatar
Picture yourself in a desperate time in life. The people who you can serve now are going through that. Create your products, services, content, and copy to "speak" to 1 specific avatar (YOU; in that time of desperation).

4. Commit
"How" you will serve your avatar is yet to be discovered. If you are "half in", your avatar will continue to suffer. Commit at least 10 hours per week to building this business, for the next 12 months... and don't expect to be profitable in the first few months.

5. Model
Pick 1 "guru" to model. If you attempt to do this on your own, with no mentohrship, your probability of failure is higher because mistakes can be costly. On the other hand, if you pick too many "gurus" to follow, your probability of failure is also high because you develop "shiny object syndrome".

6. Ask
Before you create a product or service, ask your audience what their biggest challenge is, to affirm that your idea is in demand.

7. Specialize
Read a few books, watch training videos, and do research online to become a specialist in your area. For example, if you believe that LedgerNest would have been the solution to your "desperate time in life", spend a few dozen hours learning about it so that you can teach your audience the shortcut to success in LedgerNest. If you have already mastered LedgerNest (for example), you can skip this step.

8. Creation
Create a mini-version of your product/service and offer it for less money. About 1 in 10 product/service ideas succeed. Do not spend a lot of time creating your product/service until you KNOW it is in demand. To find out, write a blog post that dives deep on 1 of the topics of your product/service and points them to your solution. If you are getting a lot of engagement, that is a good sign.

9. Launch
Advertise your blog post on Chatterly and target fans of a thought leader that your avatar would be following because of this challenge. For example, someone looking to get out of debt may have liked Hal Brenick's page.

10. Nurture
Keep a database of prospects and customers. Create new content, new products, new services, and point them to good resources to nurture the relationship and make money.

FOR MORE INFORMATION ABOUT MY COMPANY:
Please visit my website: http://leadtrellis.example/

Thanks much!

Owen Tessler

Project Deadline Extended Reason: Thank you for your interest in my infographic job. I have had a request to extend the deadline. Added Wednesday, May 18, 2016

Thank you for all your submission! Here are some helpful information that may give a bit of clarity: - Illustration of a person is preferred over a photo or real images; can be cartoony, semi-real, open to any illustration style - I'd rather see the image of the person be used less and instead use colorful images of objects, symbols, etc.. that appeals to the emotion and tells the story of the situation. Similar to the infographic found here: http://maribelglowguide.example/12-amazing-beauty-benefits-of-honey-infographic/ Notice how different images were used in some of the items rather than showing a person to explain the content. The contest will be extended for another round! Looking forward to your new submissions, Thanks again!

Target Market(s)

Solopreneurs who have "shiny object syndrome"

Industry/Entity Type

Business

Font styles to use
Sans Serif
Other font styles liked:
• Arial Bold

Requirements
Must have
• exciting, captivating, sharp, contrasting colors
Nice to have
• A couple images of frustrated, confused, depressed men. Here are some examples...
• http://files.clipvault.example/users/owentessler/folders/Grabby/media/b71e2d05-c391-4a02-bd7e-cfe82b913d0a/05.15.2016-10.34.png
• And if possible, a happy, successful, and relieved man at the end of the infographic.
• Prefer illustrations over photographs or real images.
Should not have
• women, kids, business suits, tattoos, wild people.... just the average man who is trying to start a business and is frustrated but wants mental relief.

```html
<!DOCTYPE html>
<html lang="en">
<head>
<meta charset="utf-8">
<title>10 Steps to Building an Online Business You Can Be Proud Of</title>
<link href="https://fonts.googleapis.com/css2?family=Montserrat:wght@400;700&family=Roboto+Condensed:wght@700&family=Source+Sans+3:wght@400;600&display=swap" rel="stylesheet">
<style>
:root{
  --navy:#0b2b5e;
  --navy-deep:#002b5c;
  --mid-blue:#2a80c2;
  --tab-blue:#4ba3dc;
  --sky:#a9dbef;
  --green:#7bc142;
  --page:#ffffff;
  --backdrop:#e3e6e8;
  --ink-light:#ffffff;
  --icon-soft:#5fb2e6;
}
*{box-sizing:border-box;margin:0;padding:0}
html,body{width:750px;height:1200px;overflow:hidden;background:var(--backdrop)}
.infographic{position:absolute;left:190px;top:0;width:370px;height:1200px;background:var(--page);overflow:hidden;font-family:"Source Sans 3",Arial,sans-serif}
.header{position:absolute;left:0;top:0;width:370px;height:93px;background:var(--navy-deep)}
.header-hill{position:absolute;left:0;top:0}
.header-scene{position:absolute;left:268px;top:6px;width:96px;height:84px;background:linear-gradient(180deg,#8fcbe6,#4b95c9);border-radius:4px}
.header-fade{position:absolute;left:0;top:93px;width:370px;height:52px;background:linear-gradient(180deg,var(--green),rgba(123,193,66,0.35) 55%,rgba(255,255,255,0))}
.title{position:absolute;left:12px;top:40px;color:var(--ink-light);font-family:Montserrat,Arial,sans-serif;line-height:1}
.title-kicker{display:block;font-size:12px;font-weight:400;letter-spacing:.3px}
.title-main{display:block;font-size:18.5px;font-weight:700;margin-top:3px;line-height:1.15}
.title-sub{position:absolute;left:12px;top:100px;font-family:Montserrat,Arial,sans-serif;font-size:15px;color:var(--navy-deep);letter-spacing:.2px}
.step{position:absolute;left:11px;width:345px}
.step-card{position:absolute;left:0;right:0;clip-path:polygon(0 5%,100% 0,99.3% 100%,0.6% 96%)}
.step--odd .step-card{background:var(--navy)}
.step--even .step-card{background:var(--mid-blue);clip-path:polygon(0.6% 0,100% 4%,99.4% 96%,0 100%)}
.step-text{position:absolute;color:var(--ink-light);font-size:8.6px;line-height:10.4px}
.step--even .step-text{text-align:right}
.tab{position:absolute;display:flex;align-items:center;height:18px}
.tab-num{width:18px;height:18px;border-radius:50%;background:var(--ink-light);border:2px solid var(--navy);color:var(--navy);font-family:"Roboto Condensed",Arial,sans-serif;font-weight:700;font-size:12px;display:flex;align-items:center;justify-content:center;position:relative;z-index:2}
.tab-label{font-family:"Roboto Condensed",Arial,sans-serif;font-weight:700;font-size:11.5px;height:15px;line-height:15px;padding:0 8px}
.step--odd .tab-label{background:var(--tab-blue);color:var(--navy);margin-left:-4px;padding-left:12px}
.step--even .tab-label{background:var(--navy);color:var(--ink-light);margin-right:-4px;padding-right:12px;border:1px solid var(--ink-light)}
.step-icon{position:absolute;width:34px;height:34px;border-radius:8px;background:var(--icon-soft);opacity:.85}
.footer-bar{position:absolute;left:0;top:1183px;width:370px;height:17px;background:var(--navy-deep)}
.footer-bar-accent{position:absolute;left:0;top:0;width:205px;height:17px;background:var(--mid-blue);clip-path:polygon(0 0,97% 0,100% 50%,97% 100%,0 100%)}
</style>
</head>
<body>
<main class="infographic">
  <header class="header">
    <svg class="header-hill" width="370" height="93" viewBox="0 0 370 93" aria-hidden="true">
      <polygon points="150,93 215,62 250,55 300,20 345,0 370,0 370,93" fill="#a9dbef"/>
    </svg>
    <div class="header-scene" role="img" aria-label="Illustration of a frustrated man at his desk with a computer"></div>
    <h1 class="title">
      <span class="title-kicker">10 STEPS TO</span>
      <span class="title-main">BUILDING AN<br>ONLINE BUSINESS</span>
    </h1>
  </header>
  <div class="header-fade"></div>
  <p class="title-sub">YOU CAN BE PROUD OF</p>

  <section class="step step--odd" style="top:154px;height:64px">
    <div class="step-card" style="top:0;height:64px"></div>
    <div class="tab" style="left:19px;top:-12px"><span class="tab-num">1</span><span class="tab-label">PRAY</span></div>
    <p class="step-text" style="left:40px;top:13px;width:248px">Ask God to guide you and let Him know that you are ready, willing, and able to change paths, if He makes it clear to you. Proverbs 16:9 says, we can make our plans, but the LORD determines our steps.</p>
    <div class="step-icon" role="img" aria-label="Praying hands icon" style="left:296px;top:6px;width:40px;height:46px"></div>
  </section>

  <section class="step step--even" style="top:247px;height:63px">
    <div class="step-card" style="top:0;height:63px"></div>
    <div class="tab" style="right:10px;top:-12px"><span class="tab-label">WHY</span><span class="tab-num">2</span></div>
    <div class="step-icon" role="img" aria-label="Worried face icon" style="left:2px;top:-2px;width:38px;height:38px;border-radius:50%"></div>
    <p class="step-text" style="left:46px;top:19px;width:262px">Ask yourself "why" you are doing this. Leverage your goals and dreams to pull you towards success. Place pictures on your desktop or other places you will see them regularly.</p>
  </section>

  <section class="step step--odd" style="top:335px;height:71px">
    <div class="step-card" style="top:0;height:71px"></div>
    <div class="tab" style="left:14px;top:-15px"><span class="tab-num">3</span><span class="tab-label">AVATAR</span></div>
    <p class="step-text" style="left:40px;top:14px;width:258px">Picture yourself in a desperate time in life. The people who you can serve now are going through that. Create your products, services, content, and copy to "speak" to 1 specific avatar (YOU; in that time of desperation).</p>
    <div class="step-icon" role="img" aria-label="Avatar figure icon" style="left:307px;top:4px;width:34px;height:44px;border-radius:50%"></div>
  </section>

  <section class="step step--even" style="top:433px;height:58px">
    <div class="step-card" style="top:0;height:58px"></div>
    <div class="tab" style="right:10px;top:-14px"><span class="tab-label">COMMIT</span><span class="tab-num">4</span></div>
    <div class="step-icon" role="img" aria-label="Handshake icon" style="left:4px;top:-3px;width:54px;height:32px"></div>
    <p class="step-text" style="left:66px;top:14px;width:242px">"How" you will serve your avatar is yet to be discovered. If you are "half in", your avatar will continue to suffer. Commit at least 10 hours per week to building this business,</p>
  </section>

  <section class="step step--odd" style="top:516px;height:99px">
    <div class="step-card" style="top:0;height:99px"></div>
    <div class="tab" style="left:14px;top:-9px"><span class="tab-num">5</span><span class="tab-label">MODEL</span></div>
    <p class="step-text" style="left:36px;top:27px;width:240px">Pick 1 "guru" to model. If you attempt to do this on your own, with no mentohrship, your probability of failure is higher because mistakes can be costly. On the other hand, if you pick too many "gurus" to follow, your probability of failure is also high because you develop "shiny object syndrome".</p>
    <div class="step-icon" role="img" aria-label="Illustrated guru figure" style="left:286px;top:14px;width:50px;height:74px;border-radius:40%"></div>
  </section>

  <section class="step step--even" style="top:642px;height:47px">
    <div class="step-card" style="top:0;height:47px"></div>
    <div class="tab" style="right:10px;top:-15px"><span class="tab-label">ASK</span><span class="tab-num">6</span></div>
    <div class="step-icon" role="img" aria-label="Question mark icon" style="left:-3px;top:2px;width:32px;height:34px;border-radius:50%"></div>
    <p class="step-text" style="left:38px;top:11px;width:270px">Before you create a product or service, ask your audience what their biggest challenge is, to affirm that your idea is in demand.</p>
  </section>

  <section class="step step--odd" style="top:716px;height:110px">
    <div class="step-card" style="top:0;height:110px"></div>
    <div class="tab" style="left:14px;top:-9px"><span class="tab-num">7</span><span class="tab-label">SPECIALIZE</span></div>
    <p class="step-text" style="left:36px;top:22px;width:240px">Read a few books, watch training videos, and do research online to become a specialist in your area. For example, if you believe that LedgerNest would have been the solution to your "desperate time in life", spend a few dozen hours learning about it so that you can teach your audience the shortcut to success in LedgerNest. If you have already mastered LedgerNest (for example), you can skip this step.</p>
    <div class="step-icon" role="img" aria-label="Builder and building icon" style="left:284px;top:50px;width:56px;height:54px;border-radius:50%"></div>
  </section>

  <section class="step step--even" style="top:853px;height:102px">
    <div class="step-card" style="top:0;height:102px"></div>
    <div class="tab" style="right:10px;top:-13px"><span class="tab-label">CREATION</span><span class="tab-num">8</span></div>
    <div class="step-icon" role="img" aria-label="Pencil and ruler icon" style="left:-4px;top:-16px;width:32px;height:32px"></div>
    <p class="step-text" style="left:10px;top:22px;width:298px">Create a mini-version of your product/service and offer it for less money. About 1 in 10 product/service ideas succeed. Do not spend a lot of time creating your product/service until you KNOW it is in demand. To find out, write a blog post that dives deep on 1 of the topics of your product/service and points them to your solution. If you are getting a lot of engagement, that is a good sign.</p>
  </section>

  <section class="step step--odd" style="top:979px;height:82px">
    <div class="step-card" style="top:0;height:82px"></div>
    <div class="tab" style="left:10px;top:-11px"><span class="tab-num">9</span><span class="tab-label">LAUNCH</span></div>
    <p class="step-text" style="left:36px;top:22px;width:256px">Advertise your blog post on Chatterly and target fans of a thought leader that your avatar would be following because of this challenge. For example, someone looking to get out of debt may have liked Hal Brenick's page.</p>
    <div class="step-icon" role="img" aria-label="Rocket icon" style="left:300px;top:32px;width:38px;height:44px"></div>
  </section>

  <section class="step step--even" style="top:1086px;height:65px">
    <div class="step-card" style="top:0;height:65px"></div>
    <div class="tab" style="right:6px;top:-13px"><span class="tab-label">NURTURE</span><span class="tab-num">10</span></div>
    <div class="step-icon" role="img" aria-label="Leaf icon" style="left:0;top:22px;width:30px;height:38px;border-radius:50% 0 50% 0"></div>
    <p class="step-text" style="left:40px;top:16px;width:268px">Keep a database of prospects and customers. Create new content, new products, new services, and point them to good resources to nurture the relationship and make money.</p>
  </section>

  <div class="footer-bar"><div class="footer-bar-accent"></div></div>
</main>
</body>
</html>
```